Contact Page for Design Number 58190476

I would like to request a "Contact Us" page for the site delivered in Design Number 58190476.

1) The page should be responsive on desktop, tablet and mobile phone.
2) The page should have the following fields:
- Name (text)
- Email address (text)
- Topic (list: Question, Complaint, Appreciation)
- Subject (text)
- Message (textarea)
- Send (button)
3) I would like to get the html and css code.
4) I need to know explicitly the changes done to the css of the final version of Design Number 58190476 required for the new "Contact Us" page.

```html
<!DOCTYPE html>
<html lang="en">
<head>
<meta charset="UTF-8">
<title>Contact Us</title>
<link rel="stylesheet" href="https://fonts.googleapis.com/css2?family=Poppins:wght@400;600;700&display=swap">
<style>
  :root {
    --navy: #203556;
    --navy-deep: #1a2c4a;
    --label: #0f2344;
    --text: #333a44;
    --field-border: #dcdcdc;
    --page: #ffffff;
    --accent: #f04b4b;
    --accent-dark: #c73a3b;
  }
  * { box-sizing: border-box; margin: 0; padding: 0; }
  html, body {
    width: 1200px;
    height: 2394px;
    overflow: hidden;
    background: var(--page);
    font-family: "Poppins", sans-serif;
  }
  .contact-page {
    position: relative;
    width: 1200px;
    height: 2394px;
  }
  .hero {
    position: absolute;
    left: 0;
    top: 0;
    width: 1200px;
    height: 444px;
  }
  .hero svg { display: block; }
  .hero-title {
    position: absolute;
    left: 0;
    right: 0;
    top: 176px;
    text-align: center;
    color: #ffffff;
    font-weight: 700;
    font-size: 80px;
    line-height: 100px;
    letter-spacing: 1px;
  }
  .contact-form {
    position: absolute;
    left: 138px;
    top: 0;
    width: 924px;
  }
  .field-label {
    position: absolute;
    left: 0;
    color: var(--label);
    font-weight: 600;
    font-size: 41px;
    line-height: 50px;
  }
  .field-control {
    position: absolute;
    left: 0;
    width: 924px;
    height: 134px;
    background: #ffffff;
    border: 2px solid var(--field-border);
    border-radius: 6px;
    box-shadow: 0 8px 22px rgba(0, 0, 0, 0.07);
    padding: 0 40px;
    font-family: "Poppins", sans-serif;
    font-size: 41px;
    color: var(--text);
    appearance: none;
    outline: none;
  }
  .field-control::placeholder { color: var(--text); opacity: 1; }
  .field-textarea {
    height: 424px;
    padding-top: 32px;
    resize: none;
    line-height: 56px;
  }
  .select-wrap { position: absolute; left: 0; width: 924px; height: 134px; }
  .select-wrap .field-control { top: 0; }
  .select-chevron {
    position: absolute;
    right: 36px;
    top: 57px;
    pointer-events: none;
  }
  .send-button {
    position: absolute;
    left: 278px;
    top: 2030px;
    width: 369px;
    height: 130px;
    border: none;
    border-radius: 65px;
    background: var(--accent);
    box-shadow: 0 8px 0 var(--accent-dark);
    color: #ffffff;
    font-family: "Poppins", sans-serif;
    font-weight: 700;
    font-size: 41px;
    letter-spacing: 2px;
  }
</style>
</head>
<body>
<main class="contact-page">
  <header class="hero">
    <svg width="1200" height="444" viewBox="0 0 1200 444" aria-hidden="true">
      <defs>
        <linearGradient id="heroFill" x1="0" y1="0" x2="1" y2="1">
          <stop offset="0" stop-color="#22385a"/>
          <stop offset="1" stop-color="#1c3051"/>
        </linearGradient>
      </defs>
      <path d="M0 0 H1200 V308 Q600 580 0 308 Z" fill="url(#heroFill)" stroke="var(--navy-deep)" stroke-width="2"/>
    </svg>
    <h1 class="hero-title">Contact Us</h1>
  </header>

  <form class="contact-form">
    <label class="field-label" for="name" style="top:508px">Name</label>
    <input class="field-control" id="name" type="text" placeholder="Enter Your Name" style="top:574px">

    <label class="field-label" for="email" style="top:742px">Email</label>
    <input class="field-control" id="email" type="text" placeholder="Enter Email Address" style="top:808px">

    <label class="field-label" for="topic" style="top:976px">Topic</label>
    <div class="select-wrap" style="top:1042px">
      <select class="field-control" id="topic">
        <option>Question</option>
        <option>Complaint</option>
        <option>Appreciation</option>
      </select>
      <svg class="select-chevron" width="24" height="16" viewBox="0 0 24 16" aria-hidden="true">
        <path d="M4 4 L12 12 L20 4" fill="none" stroke="var(--label)" stroke-width="3.5" stroke-linecap="round" stroke-linejoin="round"/>
      </svg>
    </div>

    <label class="field-label" for="subject" style="top:1212px">Subject</label>
    <input class="field-control" id="subject" type="text" placeholder="Enter Your Subject" style="top:1278px">

    <label class="field-label" for="message" style="top:1442px">Message</label>
    <textarea class="field-control field-textarea" id="message" placeholder="Type Your Message" style="top:1508px"></textarea>
  </form>

  <button class="send-button" type="submit">SEND</button>
</main>
</body>
</html>
```